Web design for Digital Marketing Agency

Hello,
the name of our agency is "Bright Lantern" with the idea that we make Bright Lantern for our client count. You can find our logo attached. Use blue tone similar to it a modern sans serif form that fits the design.
We need a web design similar to this one:
https: // larkfield-studio. de /
What I like about this design:
- clear navigation with personalized Pic for phone number and clear call to action in nav bar (which is then repeated in hero image)
- the hero image having custom cartoon represtation giving a visual impression of what the company does (in our case paid adwords on different channels, like Wexly Ads, Tribbon etc; and analyzing data and optimizing the website based on that)
-a clear cut structure that goes on with similar cartoons when appropriate
- using bright background colors for sections
- lots of space so content can breath
The following sections are needed in this order:
-navbar
-hero image with text:
"Digital marketing for companies who know that Bright Lantern counts.
We always help you to achieve the best in every digital transaction. Because like in real life, you don't get a second channel for your first impression. "
Services Section:
1.) Paid advertising
2.) Analytics & Optimization
3.) Chatbots
4.) E-commerce shops
-Explaining the Service Secion (the section explaining the service that is chose by the user above 1/3 image / 2/3 text - image should also be a cartoon fitting in style to overall pic and representing the service that will be explained)
- Bright Lantern Concept
2 rings similar to above website
- the process section
- what customer are saying section
-contact form section
-footer
Target Market(s)
Companies seeking to increase sales online / generate new lead online. Main focus ecommerce but also traditional companies like real estate or lawyers
Number of Pages Required
1 page
Font styles to use
Look and feel
Each slider illustrates characteristics of the customer's brand and the style your logo design should communicate.

```html
<!DOCTYPE html>
<html lang="en">
<head>
<meta charset="utf-8">
<title>Bright Lantern – Digital Marketing</title>
<link href="https://fonts.googleapis.com/css2?family=Roboto:ital,wght@0,400;0,500;0,700;1,400&family=Raleway:wght@400;500;600&display=swap" rel="stylesheet">
<style>
:root{
  --blue:#2f8fd3;
  --blue-dark:#1f78bd;
  --blue-soft:#b5dcef;
  --blue-mid:#3a93d2;
  --ink:#1c1c1c;
  --navy:#1b2a52;
  --text:#555;
  --line:#c9d3dc;
  --grey-1:#f6f6f6;
  --grey-2:#ececec;
  --white:#fff;
}
*{box-sizing:border-box;margin:0;padding:0}
html,body{width:1200px;height:4082px;overflow:hidden}
body{position:relative;background:var(--white);font-family:"Raleway",sans-serif;color:var(--text)}
.abs{position:absolute}
.btn{position:absolute;background:var(--blue);color:var(--white);font-family:"Roboto",sans-serif;font-weight:500;font-size:14px;display:flex;align-items:center;justify-content:center;letter-spacing:.3px;border-radius:2px}
.art{position:absolute;border-radius:14px}
h1,h2,h3,h4{font-family:"Roboto",sans-serif;color:var(--ink)}

/* nav */
.brand{position:absolute;left:108px;top:30px;display:flex;align-items:center;gap:12px;font-family:"Roboto",sans-serif;font-weight:500;font-size:22px;color:var(--blue);letter-spacing:.5px}
.brand .dot{width:36px;height:36px;border-radius:50%;background:var(--blue)}
.nav a{position:absolute;top:36px;font-family:"Roboto",sans-serif;font-size:14px;color:#333;text-decoration:none}
.nav a.active{color:var(--blue)}
.phone{position:absolute;left:848px;top:38px;display:flex;align-items:center;gap:8px;font-family:"Raleway",sans-serif;font-weight:600;font-size:15px;color:var(--blue)}

/* hero */
.hero-title{position:absolute;left:360px;top:268px;width:480px;text-align:center;font-size:35px;line-height:38px;font-weight:700}
.hero-text{position:absolute;left:395px;top:402px;width:410px;text-align:center;font-family:"Roboto",sans-serif;font-size:15px;line-height:25px;color:#444}

/* sections */
.sec-title{position:absolute;left:0;width:1200px;text-align:center;font-size:32px;font-weight:700}
.sec-sub{position:absolute;left:320px;width:560px;text-align:center;font-size:13px;line-height:21px;color:#444}
.svc-title{position:absolute;font-size:24px;font-weight:700;letter-spacing:.2px}
.svc-title::after{content:"";position:absolute;left:0;top:40px;width:50px;height:3px;background:var(--blue)}
.svc-text{position:absolute;width:360px;font-size:14px;line-height:23.5px;color:#444;text-align:justify}
.badge{position:absolute;width:38px;height:38px;border-radius:50%;background:var(--blue);border:4px solid #d9ecf8;color:#fff;font-family:"Roboto",sans-serif;font-size:13px;display:flex;align-items:center;justify-content:center;box-shadow:0 2px 6px rgba(0,0,0,.2)}

.band{position:absolute;left:0;width:1200px}
.concept-text{position:absolute;left:196px;width:410px;font-size:13px;line-height:23px;color:#555}
.venn-label{position:absolute;font-family:"Raleway",sans-serif;font-weight:600;font-size:15px;color:#1f3555}

.step-icon{position:absolute;width:62px;height:62px;border-radius:50%;background:var(--blue-dark);border:4px solid #fff;box-shadow:0 0 0 2px var(--blue)}
.step-title{position:absolute;left:712px;font-family:"Roboto",sans-serif;font-weight:700;font-size:15px;color:#222}
.step-text{position:absolute;left:712px;width:260px;font-family:"Roboto",sans-serif;font-size:12.5px;line-height:23px;color:#333}

.quote{position:absolute;left:442px;top:3112px;width:530px;font-family:"Roboto",sans-serif;font-style:italic;font-size:13.5px;line-height:24px;color:#444}
.qmark{position:absolute;font-family:"Roboto",sans-serif;font-size:90px;font-weight:700;color:#d7d7d7;line-height:1}

.field{position:absolute;background:#fff;border:1px solid #cfcfcf;font-family:"Roboto",sans-serif;font-size:13px;color:#444;padding:11px 14px}

/* footer */
.footer{position:absolute;left:0;top:3752px;width:1200px;height:330px;background:var(--blue-mid);color:#fff}
.footer h4{position:absolute;top:68px;color:#fff;font-weight:500;font-size:17px}
.footer ul{position:absolute;top:98px;list-style:none;font-family:"Roboto",sans-serif;font-size:12.5px;line-height:25.5px}
.social{position:absolute;top:155px;width:18px;height:18px;border-radius:50%;border:2px solid #fff}
</style>
</head>
<body>

<!-- navigation -->
<div class="brand"><span class="dot"></span>BRIGHT LANTERN</div>
<nav class="nav">
  <a class="active" style="left:464px">Home</a>
  <a style="left:535px">About</a>
  <a style="left:602px">Services</a>
  <a style="left:685px">Process</a>
  <a style="left:765px">Contact</a>
</nav>
<div class="phone">
  <svg width="16" height="16" viewBox="0 0 16 16"><circle cx="8" cy="8" r="8" fill="var(--blue)"/><path d="M5 4.5c.5-.5 1.2-.3 1.4.3l.4 1.2-.9.8c.4.9 1.2 1.7 2.1 2.1l.8-.9 1.2.4c.6.2.8.9.3 1.4-.6.7-1.6.9-2.5.4-1.3-.7-2.4-1.8-3.1-3.1-.5-.9-.3-1.9.3-2.6z" fill="#fff"/></svg>
  125 555 0148
</div>
<div class="btn" style="left:983px;top:32px;width:108px;height:33px;font-size:12.5px">Get Started</div>

<!-- hero -->
<svg class="abs" style="left:0;top:120px" width="1200" height="580" viewBox="0 0 1200 580">
  <path d="M570 22 Q605 0 640 22 L960 268 Q985 288 960 308 L640 550 Q605 572 570 550 L230 300 Q205 282 230 262 Z" fill="none" stroke="var(--blue-soft)" stroke-width="1.5"/>
</svg>
<div class="art" role="img" aria-label="Isometric illustration of marketers working with screens, charts and ad targets" style="left:58px;top:127px;width:314px;height:310px;background:linear-gradient(135deg,#e6eefb,#f7e7bf 60%,#eef3fb)"></div>
<div class="art" role="img" aria-label="Isometric illustration of analytics dashboards, folders and people analysing data" style="left:785px;top:349px;width:360px;height:325px;background:linear-gradient(135deg,#eef2fb,#f8cfa8 55%,#dfe9f8)"></div>
<svg class="abs" style="left:572px;top:205px" width="56" height="56" viewBox="0 0 56 56"><circle cx="30" cy="32" r="20" fill="#e4f0fa"/></svg>
<h1 class="hero-title">Digital Marketing for companies who know that Bright Lantern counts.</h1>
<p class="hero-text">We always help you to achieve the best in every digital transaction. Because like in real life, you don't get a second channel for your first impression.</p>
<div class="btn" style="left:529px;top:502px;width:152px;height:42px">LEARN MORE</div>

<!-- services -->
<h2 class="sec-title" style="top:750px">OUR SERVICES</h2>
<p class="sec-sub" style="top:798px">Nemo enim ipsam voluptatem quia voluptas sit aspernatur aut odit aut fugit, sed quia consequuntur magni dolores eos qui ratione voluptatem sequi nesciunt</p>

<svg class="abs" style="left:0;top:940px" width="1200" height="1000" viewBox="0 0 1200 1000">
  <g fill="none" stroke="var(--line)" stroke-width="1.5">
    <path d="M211 50 V236 Q211 254 229 254 H1014"/>
    <path d="M1014 254 Q1032 254 1032 272 V575 Q1032 593 1014 593 H226 Q208 593 208 611 V912 Q208 930 226 930 H583 Q601 930 601 948 V982"/>
  </g>
  <path d="M595 976 L601 984 L607 976" fill="none" stroke="var(--line)" stroke-width="1.5"/>
</svg>

<div class="badge" style="left:192px;top:953px">01</div>
<div class="art" role="img" aria-label="Illustration of an advertising dashboard on a blue circle with targets and charts" style="left:246px;top:924px;width:348px;height:230px;background:radial-gradient(circle at 50% 52%,#2d8fe0 0 33%,#eef4fb 34%)"></div>
<h3 class="svc-title" style="left:637px;top:940px">PAID ADVERTISING</h3>
<p class="svc-text" style="left:637px;top:990px">Nemo enim ipsam voluptatem quia voluptas sit aspernatur aut odit aut fugit, sed quia consequuntur magni dolores eos qui ratione voluptatem sequi nesciunt. Neque porro quisquam est,</p>
<div class="btn" style="left:636px;top:1105px;width:130px;height:41px">LEARN MORE</div>

<div class="badge" style="left:992px;top:1344px">02</div>
<h3 class="svc-title" style="left:217px;top:1254px">ANALYTICS &amp; OPTIMIZATION</h3>
<p class="svc-text" style="left:215px;top:1310px;width:351px">Nemo enim ipsam voluptatem quia voluptas sit aspernatur aut odit aut fugit, sed quia consequuntur magni dolores eos qui ratione voluptatem sequi nesciunt. Neque porro quisquam est,</p>
<div class="btn" style="left:212px;top:1422px;width:130px;height:44px">LEARN MORE</div>
<div class="art" role="img" aria-label="Illustration of a monitor with analytics charts and a person with a magnifier" style="left:626px;top:1213px;width:341px;height:309px;background:linear-gradient(160deg,#f4f7fb,#3c8fe6 60%,#d9ebfb)"></div>

<div class="badge" style="left:190px;top:1682px">03</div>
<div class="art" role="img" aria-label="Illustration of a chatbot robot standing on a smartphone" style="left:222px;top:1553px;width:341px;height:301px;background:radial-gradient(circle at 50% 60%,#1d68e0 0 30%,#eef2fb 31%)"></div>
<h3 class="svc-title" style="left:628px;top:1611px">CHATBOTS</h3>
<p class="svc-text" style="left:628px;top:1665px">Nemo enim ipsam voluptatem quia voluptas sit aspernatur aut odit aut fugit, sed quia consequuntur magni dolores eos qui ratione voluptatem sequi nesciunt. Neque porro quisquam est,</p>
<div class="btn" style="left:628px;top:1783px;width:130px;height:43px">LEARN MORE</div>

<div class="btn" style="left:531px;top:1929px;width:141px;height:43px">GET STARTED</div>

<!-- concept -->
<div class="band" style="top:2019px;height:438px;background:var(--grey-1)"></div>
<h2 class="abs" style="left:196px;top:2112px;font-size:27px;font-weight:700">BRIGHT LANTERN</h2>
<p class="concept-text" style="top:2160px">Nemo enim ipsam voluptatem quia voluptas sit aspernatur aut odit aut fugit, sed quia consequuntur magni dolores eos</p>
<p class="concept-text" style="top:2229px">qui ratione voluptatem sequi nesciunt. Neque porro quisquam est, Nemo enim ipsam voluptatem quia voluptas sit aspernatur aut odit aut fugit, sed quia consequuntur magni dolores eos qui ratione</p>
<div class="btn" style="left:197px;top:2322px;width:127px;height:42px">LEARN MORE</div>
<svg class="abs" style="left:640px;top:2098px" width="400" height="250" viewBox="0 0 400 250">
  <defs><clipPath id="venn-left"><circle cx="122" cy="122" r="120"/></clipPath></defs>
  <circle cx="122" cy="122" r="120" fill="var(--blue-soft)"/>
  <circle cx="279" cy="122" r="120" fill="var(--blue-soft)"/>
  <circle cx="279" cy="122" r="120" fill="var(--blue-dark)" clip-path="url(#venn-left)"/>
  <circle cx="200" cy="125" r="26" fill="#fff"/>
</svg>
<div class="venn-label" style="left:678px;top:2209px">LOREM IPSUM</div>
<div class="venn-label" style="left:898px;top:2209px">LOREM IPSUM</div>

<!-- process -->
<div class="band" style="top:2457px;height:518px;background:var(--grey-2)"></div>
<div class="art" role="img" aria-label="Illustration of a team assembling puzzle pieces around a table beside a chart board" style="left:206px;top:2528px;width:396px;height:341px;background:linear-gradient(140deg,#dfe7f7,#f2b23c 45%,#e84a4a 70%,#e6ebf5)"></div>
<h2 class="abs" style="left:632px;top:2530px;font-size:28px;font-weight:700;color:var(--navy)">OUR PROCESS</h2>
<svg class="abs" style="left:655px;top:2655px" width="10" height="150" viewBox="0 0 10 150">
  <g stroke="var(--blue)" stroke-width="1.5" fill="none"><path d="M5 2 V28 M1 23 L5 29 L9 23"/><path d="M5 102 V128 M1 123 L5 129 L9 123"/></g>
</svg>
<div class="step-icon" style="left:628px;top:2594px"></div>
<div class="step-icon" style="left:628px;top:2692px"></div>
<div class="step-icon" style="left:628px;top:2790px"></div>
<div class="step-title" style="top:2596px">Neque porro quisquam est</div>
<p class="step-text" style="top:2620px">Lorem ipsum dolor sit amet, consectetur adipiscing elit, sed do eiusmod tempor .</p>
<div class="step-title" style="left:709px;top:2699px">Sed ut perspiciatis unde omnis</div>
<p class="step-text" style="left:711px;top:2720px">Lorem ipsum dolor sit amet, consectetur adipiscing elit, sed do eiusmod tempor .</p>
<div class="step-title" style="left:711px;top:2795px">At vero eos et accusamus et</div>
<p class="step-text" style="left:711px;top:2820px">Lorem ipsum dolor sit amet, consectetur adipiscing elit, sed do eiusmod tempor .</p>

<!-- testimonials -->
<h2 class="sec-title" style="top:3043px;font-size:27px">WHAT CUSTOMER ARE SAYING</h2>
<svg class="abs" style="left:168px;top:3158px" width="20" height="30" viewBox="0 0 20 30"><path d="M16 2 L4 15 L16 28" fill="none" stroke="#666" stroke-width="2.5"/></svg>
<svg class="abs" style="left:1008px;top:3158px" width="20" height="30" viewBox="0 0 20 30"><path d="M4 2 L16 15 L4 28" fill="none" stroke="#666" stroke-width="2.5"/></svg>
<div class="abs" role="img" aria-label="Portrait photo of a smiling customer at a laptop" style="left:230px;top:3114px;width:145px;height:145px;border-radius:50%;border:3px solid var(--blue);background:linear-gradient(160deg,#dde4ea,#8a9aa8)"></div>
<div class="qmark" style="left:383px;top:3100px">&ldquo;</div>
<div class="qmark" style="left:850px;top:3195px">&rdquo;</div>
<p class="quote">Sed ut perspiciatis unde omnis iste natus error sit voluptatem accusantium doloremque laudantium, totam rem aperiam, eaque ipsa quae ab illo inventore veritatis et quasi architecto beatae vitae dicta sunt expliemo enim ipsam voluptatem quia</p>
<div class="abs" style="left:442px;top:3200px;font-family:'Roboto',sans-serif;font-weight:500;font-size:14px;color:var(--blue)">- MARA ELLISON</div>
<div class="abs" style="left:442px;top:3224px;font-family:'Roboto',sans-serif;font-weight:500;font-size:14px;color:#222">Lorem ipsum dolor sit amet</div>

<!-- contact -->
<div class="band" role="img" aria-label="Faded city skyline photo behind the contact form" style="top:3341px;height:411px;background:linear-gradient(180deg,#f3f5f7,#e9edf1)"></div>
<h2 class="sec-title" style="top:3393px;font-size:28px">CONTACT US</h2>
<p class="abs" style="left:0;width:1200px;top:3433px;text-align:center;font-family:'Roboto',sans-serif;font-size:12.5px;color:#444">Sed ut perspiciatis unde omnis iste natus error sit voluptatem accusantium doloremque laudantium</p>
<div class="field" style="left:296px;top:3470px;width:298px;height:37px">First Name :</div>
<div class="field" style="left:604px;top:3470px;width:299px;height:37px">Last Name :</div>
<div class="field" style="left:296px;top:3517px;width:298px;height:37px">Email :</div>
<div class="field" style="left:604px;top:3517px;width:299px;height:37px">Phone :</div>
<div class="field" style="left:296px;top:3565px;width:607px;height:72px">Message :</div>
<div class="btn" style="left:533px;top:3652px;width:139px;height:41px;font-size:15px">SUBMIT</div>

<!-- footer -->
<footer class="footer">
  <div class="abs" style="left:170px;top:70px;display:flex;align-items:center;gap:12px;font-family:'Roboto',sans-serif;font-weight:500;font-size:21px;letter-spacing:.5px"><span style="width:34px;height:34px;border-radius:50%;background:#fff"></span>BRIGHT LANTERN</div>
  <p class="abs" style="left:182px;top:134px;width:300px;font-family:'Roboto',sans-serif;font-size:11px;line-height:17px">Fusce tellus Sed metus augue convallis et vehicula ut pulvinar eu ante Integer orci tellus tristique vitae consequat nec porta vel lectus Nulla sit</p>
  <h4 style="left:548px">Company</h4>
  <ul style="left:548px"><li>Home</li><li>About Us</li><li>The Process</li><li>Testimonials</li><li>Contact Us</li></ul>
  <h4 style="left:728px">Resources</h4>
  <ul style="left:728px"><li>News</li><li>Partners</li><li>Support</li><li>Term of Use</li></ul>
  <h4 style="left:883px">Contact Us</h4>
  <ul style="left:883px"><li>(555) 404 1187</li><li>hello@brightlantern.co</li></ul>
  <span class="social" style="left:880px"></span>
  <span class="social" style="left:923px"></span>
  <span class="social" style="left:966px"></span>
  <span class="social" style="left:1009px"></span>
  <div class="abs" style="left:182px;top:277px;width:875px;height:1px;background:rgba(255,255,255,.5)"></div>
  <p class="abs" style="left:0;width:1200px;top:292px;text-align:center;font-family:'Roboto',sans-serif;font-size:10px">© 2020 Bright Lantern | All Rights Reserved | Disclaimer</p>
</footer>

</body>
</html>
```